VMR business card

Need a business card for a company that provides instructional design and elearning development services. The website is here: http://vantmoro.studio/

I'm attaching a current logo, as well as the old business card design. While I like to keep it clean, the old design is too simplistic for my liking. The only idea I want to reuse from the old design is placing industry jargon on the back of the card, just need a better way to present it. But if you have other ideas for the back--feel free to experiment.

Please use the colors complementary to the color we have on the website. Thank you!

```html
<!DOCTYPE html>
<html lang="en">
<head>
<meta charset="utf-8">
<title>VMR business card</title>
<link rel="stylesheet" href="https://fonts.googleapis.com/css2?family=Open+Sans:wght@400;600;700;800&family=PT+Sans+Narrow:wght@400;700&display=swap">
<style>
  :root {
    --bg: #2b2b2b;
    --paper: #ffffff;
    --teal: #1ab3b5;
    --teal-dark: #159a9c;
    --gold: #c8b57c;
    --ink: #333333;
    --rule: #555555;
    --white: #ffffff;
  }
  * { box-sizing: border-box; margin: 0; padding: 0; }
  html, body { width: 1200px; height: 907px; overflow: hidden; }
  body {
    background: var(--bg);
    font-family: "Open Sans", Arial, sans-serif;
    position: relative;
  }
  .card {
    position: absolute;
    width: 540px;
    height: 309px;
    border-radius: 3px;
    box-shadow: 0 10px 28px rgba(0,0,0,.45);
    overflow: hidden;
  }
  /* Front */
  .card-front { left: 40px; top: 299px; background: var(--paper); }
  .brand {
    position: absolute; right: 34px; top: 34px;
    display: flex; align-items: center; gap: 12px;
  }
  .brand-mark { width: 30px; height: 30px; background: var(--teal); }
  .brand-name { font-weight: 700; font-size: 40px; color: var(--gold); letter-spacing: 1px; line-height: 1; }
  .front-rule {
    position: absolute; left: 34px; right: 34px; top: 102px;
    height: 1px; background: var(--rule);
  }
  .contact {
    position: absolute; right: 34px; top: 118px;
    list-style: none; font-size: 12.5px; color: var(--ink); text-align: right;
  }
  .contact li { display: flex; justify-content: flex-end; align-items: center; gap: 8px; height: 20px; }
  .contact-icon {
    width: 15px; height: 15px; background: var(--teal);
    display: flex; align-items: center; justify-content: center;
  }
  .person { position: absolute; left: 34px; bottom: 34px; }
  .person-name {
    font-weight: 700; font-size: 17px; letter-spacing: .3px;
    padding-bottom: 3px; border-bottom: 1px solid var(--ink);
    display: inline-block;
  }
  .person-first { color: var(--teal); }
  .person-last { color: var(--gold); }
  .person-title { font-size: 13px; color: var(--ink); margin-top: 3px; }

  /* Back */
  .card-back { left: 620px; top: 299px; background: var(--teal); color: var(--white); }
  .help-stack {
    position: absolute; left: 16px; top: 0;
    width: 309px; height: 166px;
    transform-origin: top left;
    transform: translateY(309px) rotate(-90deg);
    font-weight: 800; text-transform: uppercase;
    display: flex; flex-direction: column; justify-content: center;
    padding-left: 18px;
  }
  .help-line { line-height: .95; letter-spacing: -1px; }
  .help-how, .help-can { font-size: 44px; }
  .help-we { font-size: 62px; }
  .help-help { font-size: 42px; }
  .back-divider {
    position: absolute; left: 190px; top: 22px; bottom: 22px;
    width: 1px; background: rgba(255,255,255,.8);
  }
  .jargon {
    position: absolute; left: 204px; top: 22px; right: 12px;
    list-style: none;
    font-family: "PT Sans Narrow", "Arial Narrow", sans-serif;
    font-size: 30px; line-height: 44px; text-transform: uppercase;
    letter-spacing: -.2px; white-space: nowrap;
  }
</style>
</head>
<body>
  <section class="card card-front" aria-label="Card front">
    <div class="brand">
      <span class="brand-mark"></span>
      <span class="brand-name">VMR</span>
    </div>
    <div class="front-rule"></div>
    <ul class="contact">
      <li>555-014-2290
        <span class="contact-icon"><svg width="9" height="9" viewBox="0 0 10 10"><path d="M2 1h2l1 2.5-1.3 1a6 6 0 0 0 2.8 2.8l1-1.3L10 7v2a1 1 0 0 1-1 1A8.5 8.5 0 0 1 0 2a1 1 0 0 1 1-1z" fill="#fff"/></svg></span></li>
      <li>dostrova@vantmoro.studio
        <span class="contact-icon"><svg width="10" height="8" viewBox="0 0 10 8"><rect x=".5" y=".5" width="9" height="7" fill="none" stroke="#fff"/><path d="M.5.5 5 4.5 9.5.5" fill="none" stroke="#fff"/></svg></span></li>
      <li>www.vantmoro.studio
        <span class="contact-icon"><svg width="10" height="10" viewBox="0 0 10 10"><circle cx="5" cy="5" r="4.3" fill="none" stroke="#fff"/><path d="M.7 5h8.6M5 .7c-2.4 2.6-2.4 6 0 8.6M5 .7c2.4 2.6 2.4 6 0 8.6" fill="none" stroke="#fff" stroke-width=".8"/></svg></span></li>
    </ul>
    <div class="person">
      <p class="person-name"><span class="person-first">DANIEL</span> <span class="person-last">OSTROVA</span></p>
      <p class="person-title">Managing Director</p>
    </div>
  </section>

  <section class="card card-back" aria-label="Card back">
    <div class="help-stack">
      <span class="help-line help-how">How</span>
      <span class="help-line help-can">Can</span>
      <span class="help-line help-we">We</span>
      <span class="help-line help-help">Help?</span>
    </div>
    <div class="back-divider"></div>
    <ul class="jargon">
      <li>Mobile Learning SCORM</li>
      <li>Instructional Design LMS</li>
      <li>MOOCs eLearning HTML5</li>
      <li>Adult Learning Theory</li>
      <li>Gamification Classroom</li>
      <li>xAPI Blended Learning</li>
    </ul>
  </section>
</body>
</html>
```